" A Quitavel é uma empresa que desenvolve e fornece o sistema de cobrança Quitavel para empresas de cobrança (escritórios de cobrança, assessorias de cobranças, escritórios de advogados), tais clientes chamamos de ASSESSORIAS, e também fornecemos o sistema para empresas que possuem uma grande quantidade de clientes inadimplentes e que fazem a cobrança destes clientes internamente através de um departamento de cobrança, estes clientes chamamos de CREDORES. Alguns clientes ASSESSORIAS: www.grupoltn-exemplo.com.br www.moraisetavares-exemplo.com.br www.rvrecupera-exemplo.com.br Alguns clientes CREDORES: www.linguaviva-exemplo.com www.grupovelarium-exemplo.com.br www.ronaldos-exemplo.com.br Todos os produtos e serviços que comercializamos são através da plataforma Quitavel, por exemplo, para que um cliente utilize nosso produto “Portal de Negociação” ele precisa contratar o Quitavel já que suas configurações são através do sistema, da mesma forma o serviço de “SMS”, já que as campanhas são criadas e disparadas pelo sistema Quitavel. O sistema Quitavel “nasceu” primeiro que a empresa Quitavel, já que dois dos atuais sócios possuíram uma empresa anterior de 2012 até a abertura da Quitavel em 1 de setembro de 2015. Esta empresa desenvolvia um sistema focado para assessorias de cobrança, porém em uma tecnologia antiga, e então resolveram criar um novo software com tecnologias atuais na época e para isto buscaram um investidor e juntos optaram por criar uma nova empresa, uma nova marca. Nossa logo foi construída através da plataforma Marca Pronta e gostamos muito do resultado! E estamos aqui novamente buscando que seus profissionais nos ajudem a criar novos materiais que hoje se fazem necessários para nós. "

```html
<!DOCTYPE html>
<html lang="pt-BR">
<head>
<meta charset="utf-8">
<title>Quitavel – Produtos Adicionais</title>
<link href="https://fonts.googleapis.com/css2?family=Open+Sans:wght@400;600;700;800&display=swap" rel="stylesheet">
<style>
  :root {
    --page-bg: #eef0f2;
    --navy: #123a7c;
    --blue-deep: #0c2a63;
    --grey-bar: #7d7f84;
    --text: #3d4148;
    --rule: #b9c7dc;
    --white: #ffffff;
  }
  * { box-sizing: border-box; margin: 0; padding: 0; }
  html, body {
    width: 1200px; height: 1200px; overflow: hidden;
    background: var(--page-bg);
    font-family: "Open Sans", Arial, sans-serif;
  }
  .slide {
    position: absolute; left: 0; top: 265px;
    width: 1200px; height: 670px;
    background: var(--white);
    display: flex;
    box-shadow: 0 10px 30px rgba(0,0,0,.12);
  }
  .brand-panel {
    position: relative; width: 300px; height: 100%;
    background: linear-gradient(160deg, #2a5fb0 0%, #17468f 45%, #0d2d68 100%);
    display: flex; align-items: center; justify-content: center;
  }
  .brand-panel .photo-area {
    position: absolute; inset: 0;
    background: radial-gradient(ellipse at 70% 75%, rgba(120,160,220,.35), transparent 60%),
                radial-gradient(ellipse at 30% 20%, rgba(80,120,190,.3), transparent 55%);
  }
  .brand-name {
    position: relative; color: var(--white);
    font-weight: 700; font-size: 34px; line-height: 1;
  }
  .divider-bar { width: 18px; height: 100%; background: var(--grey-bar); }
  .content { flex: 1; padding: 42px 120px 0 60px; }
  .section-title {
    color: var(--navy); font-weight: 700; font-size: 27px;
    padding-bottom: 10px; border-bottom: 2px solid var(--rule); margin-bottom: 26px;
  }
  .product { margin-bottom: 22px; }
  .product h3 { color: var(--navy); font-weight: 700; font-size: 15px; margin-bottom: 6px; }
  .product p { color: var(--text); font-size: 12.5px; line-height: 1.75; text-align: justify; }
  .cta {
    margin-top: 12px; width: 620px; background: var(--blue-deep);
    color: var(--white); padding: 30px 30px; font-size: 15px; line-height: 1.75;
    text-transform: uppercase;
  }
  .cta strong { font-weight: 800; }
  .cta .site { white-space: nowrap; }
</style>
</head>
<body>
  <main class="slide">
    <aside class="brand-panel">
      <div class="photo-area" role="img" aria-label="Foto em tons de azul de pessoa trabalhando em um notebook"></div>
      <div class="brand-name">Quitavel</div>
    </aside>
    <div class="divider-bar"></div>
    <section class="content">
      <h2 class="section-title">PRODUTOS ADICIONAIS</h2>
      <article class="product">
        <h3>E-MAIL</h3>
        <p>Envie grandes quantidades de e-mail sem bloquear o seu servidor de SMTP, com alta taxa de empregabilidade e sem prejudicar a reputação do domínio da sua empresa. Crie suas mensagens, dispare suas campanhas, responda e-mails dentro do próprio CRM.</p>
      </article>
      <article class="product">
        <h3>LOCALIZAÇÃO CADASTRAL</h3>
        <p>Encontre informações cadastrais públicas de clientes através do próprio CRM. Através dos nossos parceiros disponibilizamos consultas que retornam novos telefones, e-mail, endereços do cliente, parentes e sócios. E pague apenas as consultas de clientes localizados.</p>
      </article>
      <article class="product">
        <h3>TORPEDO DE VOZ</h3>
        <p>Entre em contato com os clientes por telefone de maneira mais fácil possível. Através deste serviço é possível enviar mensagem de voz para qualquer telefone celular ou fixo. Crie campanhas e crie novas estratégias de cobrança com base nas respostas dos clientes.</p>
      </article>
      <div class="cta">Para mais informações sobre <strong>nossos produtos e serviços</strong> acesse nosso site <strong class="site">www.quitavel-exemplo.com.br</strong></div>
    </section>
  </main>
</body>
</html>
```